BRIMCOVE is a New Zealand based aerial imaging company performing mapping, surveying and videography

I would like a business card that is contemporary and clean. The font for the business name is called Gtec Technology and I would like to have the text "AERIAL IMAGING" under the "BRIMCOVE" name in a font similar to URW Gothic or another light modern font. Brimcove performs aerial imaging projects using a hexacopter UAV. Surveying and mapping with 3D Digital Elevation Models are a focus, I also produce aerial photographs and video's including post editing.

Target Market(s)

Industrial plant managers, Property owners, Event organisers.

Industry/Entity Type

Videography

Contact Information for Business Card

BRIMCOVE AERIAL IMAGING. Owner Reid Malloway. Cell: 021 7304169. P.O. Box 8316 Dunedin, New Zealand.

Font styles to use
Other font styles liked:
• Gtec Technology

Colors
9bcb3b
33a6d7
ec1f27

Requirements
Must have
• Modern professional look.
Nice to have
• Perhaps an aerial image of a landscape who's location is not identifiable. Maybe use included image of my hexacopter on the back of the card? Not compulsory though.
Should not have
• Clip Art style images.

```html
<!DOCTYPE html>
<html lang="en">
<head>
<meta charset="UTF-8">
<title>Brimcove Aerial Imaging – Business Card</title>
<link href="https://fonts.googleapis.com/css2?family=Questrial&family=Montserrat:wght@600;700&display=swap" rel="stylesheet">
<style>
  :root {
    --page: #ffffff;
    --ink: #000000;
    --card-dark: #000000;
    --logo-white: #ffffff;
    --tagline: #e6e6e6;
    --back-blue: #6ccef5;
    --back-text: #ffffff;
  }
  * { margin: 0; padding: 0; box-sizing: border-box; }
  html, body {
    width: 1200px; height: 476px; overflow: hidden;
    background: var(--page);
  }
  .sheet { position: relative; width: 1200px; height: 476px; }

  .card { position: absolute; top: 58px; width: 551px; height: 330px; overflow: hidden; }
  .card--front { left: 38px; background: var(--page); }
  .card--back { left: 622px; width: 548px; background: var(--back-blue); }

  .front-band { position: absolute; inset: 0; width: 551px; height: 330px; }

  .brand {
    position: absolute; left: 0; right: 0; top: 42px;
    text-align: center; color: var(--logo-white);
  }
  .brand__name {
    font-family: "Questrial", sans-serif;
    font-size: 44px; line-height: 44px;
    letter-spacing: 5px;
  }
  .brand__tagline {
    margin-top: 4px;
    font-family: "Questrial", sans-serif;
    font-size: 19px; line-height: 20px;
    letter-spacing: 7.5px;
    color: var(--tagline);
  }

  .contact {
    position: absolute; left: 0; right: 0;
    text-align: center; color: var(--ink);
    font-family: "Questrial", sans-serif;
  }
  .contact__name {
    top: 164px;
    font-family: "Montserrat", sans-serif; font-weight: 700;
    font-size: 20px; line-height: 22px;
  }
  .contact__role { top: 187px; font-size: 10px; line-height: 12px; }
  .contact__cell { top: 201px; font-size: 16px; line-height: 18px; letter-spacing: .5px; }
  .contact__company { top: 262px; font-size: 13px; line-height: 15px; }
  .contact__address { top: 280px; font-size: 16px; line-height: 18px; }

  .pitch {
    position: absolute; right: 3px; top: 34px;
    text-align: right; color: var(--back-text);
    font-family: "Questrial", sans-serif;
    font-size: 0;
    letter-spacing: 1px;
  }
  .pitch__line { display: block; white-space: nowrap; height: 36px; line-height: 36px; }
  .pitch__line--tall { height: 44px; line-height: 44px; }
  .pitch__line--short { height: 34px; line-height: 34px; }
  .pitch__line > span { line-height: 0; }
  .pitch .s { font-size: 17px; }
  .pitch .m { font-size: 22px; }
  .pitch .l { font-size: 30px; }
  .pitch .xl { font-size: 44px; letter-spacing: 2px; }
  .pitch .xxl { font-size: 40px; }
  .pitch .strong { font-family: "Montserrat", sans-serif; font-weight: 600; font-size: 22px; letter-spacing: 1.5px; }
  .pitch .gap { font-size: 17px; }

  .label {
    position: absolute; top: 410px;
    font-family: "Montserrat", sans-serif; font-weight: 700;
    font-size: 18px; letter-spacing: 1.5px; color: var(--ink);
  }
  .label--front { left: 56px; }
  .label--back { left: 657px; }
</style>
</head>
<body>
<main class="sheet">
  <section class="card card--front" aria-label="Front of business card">
    <svg class="front-band" viewBox="0 0 551 330" aria-hidden="true">
      <path d="M0 0 H551 V188 Q275.5 60 0 188 Z" fill="var(--card-dark)"/>
    </svg>
    <div class="brand">
      <div class="brand__name">BRIMCOVE</div>
      <div class="brand__tagline">Aerial Imaging</div>
    </div>
    <p class="contact contact__name">Reid Malloway</p>
    <p class="contact contact__role">Owner</p>
    <p class="contact contact__cell">Cell: 021 7304169</p>
    <p class="contact contact__company">BRIMCOVE AERIAL IMAGING</p>
    <p class="contact contact__address">P.O. Box 8316 Dunedin, New Zealand.</p>
  </section>

  <section class="card card--back" aria-label="Back of business card">
    <p class="pitch">
      <span class="pitch__line"><span class="m">Brimcove</span><span class="gap"> </span><span class="s">performs</span><span class="gap"> </span><span class="xl">aerial</span></span>
      <span class="pitch__line"><span class="xl">imaging</span><span class="s">projects</span></span>
      <span class="pitch__line"><span class="s">using a</span><span class="gap"> </span><span class="strong">hexacopter UAV</span><span class="s">.</span></span>
      <span class="pitch__line"><span class="m">Surveying and mapping</span><span class="gap"> </span><span class="s">with</span></span>
      <span class="pitch__line pitch__line--tall"><span class="xxl">3D</span><span class="gap"> </span><span class="l">Digital Elevation</span></span>
      <span class="pitch__line"><span class="m">Models</span><span class="gap"> </span><span class="s">are a focus,</span><span class="gap"> </span><span class="l">aerial</span></span>
      <span class="pitch__line pitch__line--short"><span class="l">photographs and</span></span>
      <span class="pitch__line pitch__line--short"><span class="l">video's</span><span class="s">, post editing.</span></span>
    </p>
  </section>

  <p class="label label--front">FRONT CARD DESIGN</p>
  <p class="label label--back">BACK CARD DESIGN</p>
</main>
</body>
</html>
```